Next-Gen B2B Sales Negotiation App - UI Design for iOS

Develop a user-friendly dark-mode interface for a B2B sales negotiation assistant app for a company called Quorvel. The UI will showcase a single screen with features like counterparty search, agenda selection, and email drafting. Design should reflect a functional iOS app with realistic placeholder data to create a genuine experience.

Precise task description in attachment.

Target Market(s)

B2B

Requirements
Must have
• Each UI picture should look like a screen capture of an iphone
Nice to have
• The UI designs need to show the navigation and the app in use

```html
<!DOCTYPE html>
<html lang="en">
<head>
<meta charset="utf-8">
<title>Quorvel – Negotiation Assistant UI</title>
<link rel="stylesheet" href="https://fonts.googleapis.com/css2?family=Manrope:wght@400;500;600;700;800&display=swap">
<style>
  :root{
    --canvas:#94959b;
    --pink:#ea5599;
    --pink-deep:#d84587;
    --pink-text:#f05fa2;
    --card:#131016;
    --card-line:#26222b;
    --field:#1f1c24;
    --field-2:#2b2831;
    --muted:#8b8794;
    --label:#9e99a8;
    --white:#f5f3f7;
    --green:#4fbf6a;
    --tag-bg:#33172a;
    --tag-line:#5c2444;
    --blue:#3f7bff;
  }
  *{box-sizing:border-box;margin:0;padding:0}
  html,body{width:1200px;height:1200px;overflow:hidden;background:var(--canvas)}
  body{font-family:"Manrope",sans-serif;color:var(--white)}
  .stage{position:absolute;left:0;top:0;width:1932px;height:1932px;transform:scale(.62112);transform-origin:0 0;background:var(--canvas)}
  .abs{position:absolute}
  .panel{position:absolute;border-radius:44px;overflow:hidden;background:linear-gradient(180deg,#040306 0%,#0c0910 45%,#1d1127 100%)}
  .app-title{position:absolute;left:32px;top:50px;font-size:38px;font-weight:700;letter-spacing:-.5px}
  .app-sub{position:absolute;left:33px;top:103px;font-size:15px;font-weight:600;letter-spacing:3.4px;color:var(--pink-text)}
  .round-btn{position:absolute;left:466px;top:50px;width:57px;height:57px;border-radius:50%;border:1.5px solid #2c2931;background:#141118;display:flex;align-items:center;justify-content:center}

  .contact{position:absolute;width:501px;height:380px;border-radius:32px;background:var(--card);border:1.5px solid var(--card-line)}
  .tabs{position:absolute;left:11px;top:10px;width:480px;height:62px;border-radius:30px;background:#0e0c11;display:flex;padding:2px}
  .tab{flex:1;display:flex;align-items:center;justify-content:center;font-size:16px;font-weight:700;letter-spacing:1.2px;color:#a7a3b0;border-radius:28px}
  .tab.active{background:#2a2730;color:var(--white)}
  .contact-head{position:absolute;left:35px;right:35px;top:96px;display:flex;justify-content:space-between;align-items:center}
  .contact-head .t{font-size:19px;color:var(--muted)}
  .verified{font-size:16px;color:var(--green);display:flex;align-items:center;gap:9px}
  .verified::before{content:"";width:8px;height:8px;border-radius:50%;background:var(--green)}
  .field{position:absolute;left:30px;width:442px;height:97px;border-radius:20px;background:var(--field)}
  .field.focus{border:2px solid var(--pink);background:#1d1920}
  .field-icon{position:absolute;left:24px;top:25px;width:46px;height:46px;border-radius:50%;display:flex;align-items:center;justify-content:center;background:#2c2830}
  .field-icon.person{background:#3b1d2e}
  .field-label{position:absolute;left:93px;top:24px;font-size:15px;font-weight:600;letter-spacing:1.3px;color:var(--label)}
  .field-value{position:absolute;left:93px;top:47px;font-size:23px;font-weight:500}
  .caret{display:inline-block;width:2px;height:26px;background:var(--white);vertical-align:-4px;margin-left:2px}

  .section-title{position:absolute;left:33px;top:574px;font-size:22px;font-weight:600}
  .section-icon{position:absolute;left:500px;top:577px}

  .objective{position:absolute;left:27px;top:621px;width:501px;height:116px;border-radius:30px;background:linear-gradient(180deg,#141118,#18121d);border:1.5px solid var(--card-line)}
  .objective.open{height:305px}
  .obj-icon{position:absolute;left:24px;top:23px;width:57px;height:57px;border-radius:16px;background:linear-gradient(135deg,#f062a5,#b94ad6);display:flex;align-items:center;justify-content:center;box-shadow:0 6px 18px rgba(234,85,153,.35)}
  .obj-label{position:absolute;left:99px;top:29px;font-size:15px;font-weight:600;letter-spacing:1.2px;color:var(--label)}
  .obj-value{position:absolute;left:99px;top:50px;font-size:23px;font-weight:700}
  .chev{position:absolute;right:22px;top:28px;width:46px;height:46px;border-radius:50%;background:#221f27;display:flex;align-items:center;justify-content:center}
  .obj-divider{position:absolute;left:24px;right:24px;top:102px;height:1px;background:#2a2630}
  .option{position:absolute;left:24px;width:454px;height:51px;border-radius:12px;padding:0 17px;display:flex;align-items:center;justify-content:space-between;font-size:19px;font-weight:500;color:#c9c5d0}
  .option.selected{background:#24212a;color:var(--white)}

  .stat{position:absolute;top:0;width:241px;height:136px;border-radius:28px;background:linear-gradient(140deg,#1c1a2a,#110e16);border:1.5px solid #29262f}
  .stat-icon{position:absolute;left:25px;top:22px}
  .stat-value{position:absolute;left:23px;top:52px;font-size:30px;font-weight:700}
  .stat-label{position:absolute;left:23px;top:95px;font-size:15px;font-weight:600;letter-spacing:1.5px;color:#8d8aa2}

  .toggle{position:absolute;width:501px;height:70px;border-radius:35px;border:1.5px solid #27232c;background:#110e15;display:flex;padding:9px}
  .seg{flex:1;display:flex;align-items:center;justify-content:center;gap:10px;font-size:19px;font-weight:500;color:#b7b3bf;border-radius:14px}
  .seg.active{background:#2e2b35;color:var(--white)}
  .seg.ring{background:#2b2936;border:2.5px solid var(--blue);box-shadow:0 0 0 1.5px #cfdcff inset}

  .tags{position:absolute;display:flex;gap:12px}
  .tag{height:41px;padding:0 17px;border-radius:21px;background:var(--tag-bg);border:1.5px solid var(--tag-line);display:flex;align-items:center;font-size:15px;font-weight:700;color:var(--pink-text);letter-spacing:.2px}
  .tag.add{background:transparent;border-color:#36323c;color:#9e99a8;font-weight:500}

  .channel{position:absolute;width:68px;height:68px;border-radius:18px;border:1.5px solid #2f2b35;background:#161219;display:flex;align-items:center;justify-content:center;font-size:14px;font-weight:700;color:#c8c4cf}
  .channel.active{background:var(--pink);border-color:var(--pink);box-shadow:0 8px 22px rgba(234,85,153,.35)}

  .email{position:absolute;left:27px;width:501px;height:402px;border-radius:30px;background:linear-gradient(180deg,#1a1520,#150f1a);border:1.5px solid #2a2530}
  .email .lbl{position:absolute;left:30px;top:30px;font-size:15px;font-weight:600;letter-spacing:1.3px;color:var(--label)}
  .email .subj{position:absolute;left:30px;top:55px;font-size:18px;font-weight:600}
  .email .spark{position:absolute;right:36px;top:34px}
  .email .hi{position:absolute;left:30px;top:102px;font-size:21px;color:#b6b2be}
  .email .body{position:absolute;left:30px;top:142px;width:450px;font-size:21px;line-height:33px;color:#e5e2ea}
  .email .rule{position:absolute;left:30px;right:30px;top:310px;height:1px;background:#2c2731}
  .chip{position:absolute;left:30px;top:334px;height:38px;padding:0 14px;border-radius:10px;background:#221e27;display:flex;align-items:center;gap:10px;font-size:15px;color:#c8c4cf}
  .attach{position:absolute;left:242px;top:334px;height:38px;display:flex;align-items:center;gap:8px;font-size:15px;color:#9e99a8}

  .dock{position:absolute;left:27px;width:501px;height:93px;border-radius:47px;background:#121015;border:1.5px solid #29252d}
  .dock .cal{position:absolute;left:32px;top:30px}
  .dock .sep{position:absolute;left:87px;top:30px;width:1.5px;height:34px;background:#36323c}
  .send{position:absolute;left:94px;top:12px;width:393px;height:68px;border-radius:34px;background:linear-gradient(90deg,#ee5aa0,#d6467f);display:flex;align-items:center;justify-content:center;gap:14px;font-size:28px;font-weight:700;color:#fff;box-shadow:0 8px 24px rgba(234,85,153,.3)}

  .confirm{position:absolute;left:1352px;top:858px;width:458px;height:475px;border-radius:34px;overflow:hidden;background:#111013}
  .confirm-top{position:absolute;left:0;top:0;width:100%;height:208px;background:var(--pink)}
  .send-badge{position:absolute;left:197px;top:28px;width:65px;height:65px;border-radius:50%;background:rgba(255,255,255,.22);display:flex;align-items:center;justify-content:center}
  .confirm h2{position:absolute;left:0;right:0;top:112px;text-align:center;font-size:26px;font-weight:700}
  .confirm .sub{position:absolute;left:0;right:0;top:155px;text-align:center;font-size:17px;color:#ffe3ef}
  .row{position:absolute;left:32px;right:32px;height:44px;display:flex;justify-content:space-between;align-items:center;border-bottom:1.5px solid #232027}
  .row .k{font-size:17px;color:var(--muted)}
  .row .v{font-size:17px;font-weight:700}
  .btn-cancel{position:absolute;left:60px;top:386px;width:132px;height:54px;display:flex;align-items:center;justify-content:center;font-size:18px;font-weight:600;color:#c6c2cc}
  .btn-now{position:absolute;left:238px;top:386px;width:188px;height:54px;border-radius:12px;background:#fff;color:#111;display:flex;align-items:center;justify-content:center;font-size:18px;font-weight:700}

  .sent{position:absolute;left:1352px;top:1377px;width:458px;height:474px;border-radius:34px;overflow:hidden;background:radial-gradient(circle at 8% 5%,#3a1127 0,#140b12 18%,transparent 35%),radial-gradient(circle at 50% 70%,#1a1719 0,#09080a 70%)}
  .sent h2{position:absolute;left:0;right:0;top:144px;text-align:center;font-size:46px;font-weight:800}
  .sent p{position:absolute;left:0;right:0;top:210px;text-align:center;font-size:20px;color:#c1bdc7}
  .done{position:absolute;left:170px;top:271px;width:120px;height:51px;border-radius:26px;background:var(--pink);display:flex;align-items:center;justify-content:center;font-size:20px;font-weight:700}
</style>
</head>
<body>
<div class="stage">

  <!-- Main screen -->
  <section class="panel" style="left:72px;top:82px;width:557px;height:1761px">
    <div class="app-title">Quorvel</div>
    <div class="app-sub">NEGOTIATION ASSISTANT</div>
    <div class="round-btn"><svg width="26" height="26" viewBox="0 0 24 24" fill="none" stroke="#d8d4de" stroke-width="1.6" stroke-linecap="round"><line x1="3" y1="7" x2="21" y2="7"/><line x1="3" y1="17" x2="21" y2="17"/><circle cx="8" cy="7" r="2.6" fill="#141118"/><circle cx="16" cy="17" r="2.6" fill="#141118"/></svg></div>

    <div class="contact" style="left:27px;top:158px">
      <div class="tabs"><div class="tab active">COMPANY</div><div class="tab">INDIVIDUAL</div><div class="tab">GROUP</div></div>
      <div class="contact-head"><span class="t">Target Contact</span><span class="verified">Verified</span></div>
      <div class="field" style="top:137px"><div class="field-icon person"><svg width="22" height="22" viewBox="0 0 24 24" fill="none" stroke="#f06aa8" stroke-width="1.8"><circle cx="12" cy="8" r="4"/><path d="M4.5 21c1-4 4-6 7.5-6s6.5 2 7.5 6"/></svg></div><div class="field-label">NAME</div><div class="field-value">Acme Inc.</div></div>
      <div class="field" style="top:253px"><div class="field-icon"><svg width="24" height="24" viewBox="0 0 24 24" fill="none" stroke="#a9a5b0" stroke-width="1.6"><rect x="3" y="7" width="18" height="13" rx="2"/><path d="M8 7V4h8v3M9 7v13M15 7v13"/></svg></div><div class="field-label">ROLE / CONTEXT</div><div class="field-value">Sarah Chen (CEO)</div></div>
    </div>

    <div class="section-title">Strategy Configuration</div>
    <svg class="section-icon" width="26" height="26" viewBox="0 0 24 24" fill="none" stroke="#8b8794" stroke-width="1.6" stroke-linecap="round"><path d="M3 6h11M18 6h3M3 12h4M11 12h10M3 18h13M20 18h1M16 4v4M9 10v4M18 16v4"/></svg>

    <div class="objective">
      <div class="obj-icon"><svg width="30" height="30" viewBox="0 0 24 24" fill="none" stroke="#fff" stroke-width="1.8"><circle cx="12" cy="12" r="9"/><circle cx="12" cy="12" r="5"/><circle cx="12" cy="12" r="1.5" fill="#fff"/></svg></div>
      <div class="obj-label">CURRENT OBJECTIVE</div><div class="obj-value">Book a Meeting</div>
      <div class="chev"><svg width="18" height="18" viewBox="0 0 24 24" fill="none" stroke="#cfcbd6" stroke-width="2.2" stroke-linecap="round"><path d="M6 9l6 6 6-6"/></svg></div>
    </div>

    <div class="abs" style="left:0;top:756px;width:557px">
      <div class="stat" style="left:27px"><svg class="stat-icon" width="17" height="17" viewBox="0 0 24 24" fill="none" stroke="#6f9bff" stroke-width="2"><circle cx="12" cy="12" r="9"/><path d="M12 7v5l3 2"/></svg><div class="stat-value">45 min</div><div class="stat-label">DURATION</div></div>
      <div class="stat" style="left:287px"><svg class="stat-icon" width="17" height="17" viewBox="0 0 24 24" fill="none" stroke="#d8d4de" stroke-width="2"><rect x="4" y="5" width="16" height="15" rx="2"/><path d="M4 10h16M9 3v4M15 3v4"/></svg><div class="stat-value">25/01/2025</div><div class="stat-label">TARGET DATE</div></div>
      <div class="toggle" style="left:27px;top:155px"><div class="seg active"><svg width="20" height="20" viewBox="0 0 24 24" fill="none" stroke="currentColor" stroke-width="1.8"><rect x="3" y="7" width="13" height="10" rx="2"/><path d="M16 11l5-3v8l-5-3"/></svg>Online</div><div class="seg"><svg width="20" height="20" viewBox="0 0 24 24" fill="none" stroke="currentColor" stroke-width="1.8"><path d="M12 21s-7-6-7-11a7 7 0 0114 0c0 5-7 11-7 11z"/><circle cx="12" cy="10" r="2.5"/></svg>On-site</div></div>
      <div class="tags" style="left:27px;top:243px"><div class="tag">SAVE TIME</div><div class="tag">INCREASE REVENUE</div><div class="tag add">+ Add</div></div>
      <div class="channel active" style="left:33px;top:330px"><svg width="32" height="32" viewBox="0 0 24 24" fill="none" stroke="#fff" stroke-width="1.8"><rect x="3" y="5" width="18" height="14" rx="2"/><path d="M3 7l9 6 9-6"/></svg></div>
      <div class="channel" style="left:124px;top:330px">Linkr</div>
      <div class="channel" style="left:216px;top:330px"><svg width="30" height="30" viewBox="0 0 24 24" fill="none" stroke="#c8c4cf" stroke-width="1.6"><path d="M5 4h4l2 5-2.5 1.5a11 11 0 005 5L15 13l5 2v4a2 2 0 01-2 2A16 16 0 013 6a2 2 0 012-2z"/></svg></div>
      <div class="email" style="top:423px">
        <div class="lbl">SUBJECT</div><div class="subj">Proposed Meeting: Acme Inc. x Quorvel</div>
        <svg class="spark" width="30" height="30" viewBox="0 0 24 24" fill="none" stroke="#f06aa8" stroke-width="1.6" stroke-linejoin="round"><path d="M10 4l1.6 4.4L16 10l-4.4 1.6L10 16l-1.6-4.4L4 10l4.4-1.6z"/><path d="M18 3v4M16 5h4M18 16v4M16 18h4"/></svg>
        <div class="hi">Hi Sarah,</div>
        <div class="body">I would like to discuss how Quorvel can help you save time with automated negotiations. I propose a quick 30 min online meeting on Tuesday. Looking forward to your response.</div>
        <div class="rule"></div>
        <div class="chip"><svg width="16" height="16" viewBox="0 0 24 24" fill="none" stroke="#f06aa8" stroke-width="2"><path d="M6 3h8l4 4v14H6z"/><path d="M9 12h6M9 16h6"/></svg>Proposal_v1.pdf <span style="font-size:13px;margin-left:6px">×</span></div>
        <div class="attach"><span style="font-size:20px">+</span> Attach</div>
      </div>
    </div>

    <div class="dock" style="top:1638px">
      <svg class="cal" width="34" height="34" viewBox="0 0 24 24" fill="none" stroke="#b9b5c0" stroke-width="1.5"><rect x="3" y="5" width="15" height="14" rx="2"/><path d="M3 9h15M7 3v4M14 3v4"/><circle cx="17" cy="17" r="4.5" fill="#121015"/><path d="M17 15v2l1.5 1"/></svg>
      <div class="sep"></div>
      <div class="send">Send Request <svg width="28" height="28" viewBox="0 0 24 24" fill="none" stroke="#fff" stroke-width="2" stroke-linejoin="round"><path d="M21 3L10 14M21 3l-7 18-4-7-7-4z"/></svg></div>
    </div>
  </section>

  <!-- Objective expanded -->
  <section class="panel" style="left:687px;top:82px;width:557px;height:1761px">
    <div class="app-title">Quorvel</div>
    <div class="app-sub">NEGOTIATION ASSISTANT</div>
    <div class="round-btn"><svg width="26" height="26" viewBox="0 0 24 24" fill="none" stroke="#d8d4de" stroke-width="1.6" stroke-linecap="round"><line x1="3" y1="7" x2="21" y2="7"/><line x1="3" y1="17" x2="21" y2="17"/><circle cx="8" cy="7" r="2.6" fill="#141118"/><circle cx="16" cy="17" r="2.6" fill="#141118"/></svg></div>

    <div class="contact" style="left:27px;top:158px">
      <div class="tabs"><div class="tab active">COMPANY</div><div class="tab">INDIVIDUAL</div><div class="tab">GROUP</div></div>
      <div class="contact-head"><span class="t">Target Contact</span><span class="verified">Verified</span></div>
      <div class="field" style="top:137px"><div class="field-icon person"><svg width="22" height="22" viewBox="0 0 24 24" fill="none" stroke="#f06aa8" stroke-width="1.8"><circle cx="12" cy="8" r="4"/><path d="M4.5 21c1-4 4-6 7.5-6s6.5 2 7.5 6"/></svg></div><div class="field-label">NAME</div><div class="field-value">Acme Inc.</div></div>
      <div class="field" style="top:253px"><div class="field-icon"><svg width="24" height="24" viewBox="0 0 24 24" fill="none" stroke="#a9a5b0" stroke-width="1.6"><rect x="3" y="7" width="18" height="13" rx="2"/><path d="M8 7V4h8v3M9 7v13M15 7v13"/></svg></div><div class="field-label">ROLE / CONTEXT</div><div class="field-value">Sarah Chen (CEO)</div></div>
    </div>

    <div class="section-title">Strategy Configuration</div>
    <svg class="section-icon" width="26" height="26" viewBox="0 0 24 24" fill="none" stroke="#8b8794" stroke-width="1.6" stroke-linecap="round"><path d="M3 6h11M18 6h3M3 12h4M11 12h10M3 18h13M20 18h1M16 4v4M9 10v4M18 16v4"/></svg>

    <div class="objective open">
      <div class="obj-icon"><svg width="30" height="30" viewBox="0 0 24 24" fill="none" stroke="#fff" stroke-width="1.8"><circle cx="12" cy="12" r="9"/><circle cx="12" cy="12" r="5"/><circle cx="12" cy="12" r="1.5" fill="#fff"/></svg></div>
      <div class="obj-label">CURRENT OBJECTIVE</div><div class="obj-value">Book a Meeting</div>
      <div class="chev"><svg width="18" height="18" viewBox="0 0 24 24" fill="none" stroke="#cfcbd6" stroke-width="2.2" stroke-linecap="round"><path d="M6 15l6-6 6 6"/></svg></div>
      <div class="obj-divider"></div>
      <div class="option selected" style="top:116px">Technical Review <svg width="18" height="18" viewBox="0 0 24 24" fill="none" stroke="#f06aa8" stroke-width="2.2" stroke-linecap="round"><path d="M5 12l5 5 9-10"/></svg></div>
      <div class="option" style="top:173px">Product Negotiation</div>
      <div class="option" style="top:230px">Partnership Proposal</div>
    </div>

    <div class="abs" style="left:0;top:945px;width:557px">
      <div class="stat" style="left:27px"><svg class="stat-icon" width="17" height="17" viewBox="0 0 24 24" fill="none" stroke="#6f9bff" stroke-width="2"><circle cx="12" cy="12" r="9"/><path d="M12 7v5l3 2"/></svg><div class="stat-value">45 min</div><div class="stat-label">DURATION</div></div>
      <div class="stat" style="left:287px"><svg class="stat-icon" width="17" height="17" viewBox="0 0 24 24" fill="none" stroke="#d8d4de" stroke-width="2"><rect x="4" y="5" width="16" height="15" rx="2"/><path d="M4 10h16M9 3v4M15 3v4"/></svg><div class="stat-value">25/01/2025</div><div class="stat-label">TARGET DATE</div></div>
      <div class="toggle" style="left:27px;top:155px"><div class="seg active"><svg width="20" height="20" viewBox="0 0 24 24" fill="none" stroke="currentColor" stroke-width="1.8"><rect x="3" y="7" width="13" height="10" rx="2"/><path d="M16 11l5-3v8l-5-3"/></svg>Online</div><div class="seg"><svg width="20" height="20" viewBox="0 0 24 24" fill="none" stroke="currentColor" stroke-width="1.8"><path d="M12 21s-7-6-7-11a7 7 0 0114 0c0 5-7 11-7 11z"/><circle cx="12" cy="10" r="2.5"/></svg>On-site</div></div>
      <div class="tags" style="left:27px;top:243px"><div class="tag">SAVE TIME</div><div class="tag">INCREASE REVENUE</div><div class="tag add">+ Add</div></div>
      <div class="channel active" style="left:33px;top:330px"><svg width="32" height="32" viewBox="0 0 24 24" fill="none" stroke="#fff" stroke-width="1.8"><rect x="3" y="5" width="18" height="14" rx="2"/><path d="M3 7l9 6 9-6"/></svg></div>
      <div class="channel" style="left:124px;top:330px">Linkr</div>
      <div class="channel" style="left:216px;top:330px"><svg width="30" height="30" viewBox="0 0 24 24" fill="none" stroke="#c8c4cf" stroke-width="1.6"><path d="M5 4h4l2 5-2.5 1.5a11 11 0 005 5L15 13l5 2v4a2 2 0 01-2 2A16 16 0 013 6a2 2 0 012-2z"/></svg></div>
      <div class="email" style="top:423px">
        <div class="lbl">SUBJECT</div><div class="subj">Proposed Meeting: Acme Inc. x Quorvel</div>
        <svg class="spark" width="30" height="30" viewBox="0 0 24 24" fill="none" stroke="#f06aa8" stroke-width="1.6" stroke-linejoin="round"><path d="M10 4l1.6 4.4L16 10l-4.4 1.6L10 16l-1.6-4.4L4 10l4.4-1.6z"/><path d="M18 3v4M16 5h4M18 16v4M16 18h4"/></svg>
        <div class="hi">Hi Sarah,</div>
        <div class="body">I would like to discuss how Quorvel can help you save time with automated negotiations. I propose a quick 30 min online meeting on Tuesday. Looking forward to your response.</div>
      </div>
    </div>

    <div class="dock" style="top:1643px">
      <svg class="cal" width="34" height="34" viewBox="0 0 24 24" fill="none" stroke="#b9b5c0" stroke-width="1.5"><rect x="3" y="5" width="15" height="14" rx="2"/><path d="M3 9h15M7 3v4M14 3v4"/><circle cx="17" cy="17" r="4.5" fill="#121015"/><path d="M17 15v2l1.5 1"/></svg>
      <div class="sep"></div>
      <div class="send">Send Request <svg width="28" height="28" viewBox="0 0 24 24" fill="none" stroke="#fff" stroke-width="2" stroke-linejoin="round"><path d="M21 3L10 14M21 3l-7 18-4-7-7-4z"/></svg></div>
    </div>
  </section>

  <!-- Contact input focus -->
  <section class="panel" style="left:1302px;top:82px;width:558px;height:441px;background:#050407">
    <div class="contact" style="left:25px;top:28px">
      <div class="tabs"><div class="tab active">COMPANY</div><div class="tab">INDIVIDUAL</div><div class="tab">GROUP</div></div>
      <div class="contact-head"><span class="t">Target Contact</span><span class="verified">Verified</span></div>
      <div class="field focus" style="top:137px"><div class="field-icon person"><svg width="22" height="22" viewBox="0 0 24 24" fill="none" stroke="#f06aa8" stroke-width="1.8"><circle cx="12" cy="8" r="4"/><path d="M4.5 21c1-4 4-6 7.5-6s6.5 2 7.5 6"/></svg></div><div class="field-label">NAME</div><div class="field-value">Acme Inc.<span class="caret"></span></div></div>
      <div class="field" style="top:253px"><div class="field-icon"><svg width="24" height="24" viewBox="0 0 24 24" fill="none" stroke="#a9a5b0" stroke-width="1.6"><rect x="3" y="7" width="18" height="13" rx="2"/><path d="M8 7V4h8v3M9 7v13M15 7v13"/></svg></div><div class="field-label">ROLE / CONTEXT</div><div class="field-value">Sarah Chen (CEO)</div></div>
    </div>
  </section>

  <!-- On-site selection -->
  <section class="panel" style="left:1302px;top:567px;width:558px;height:248px;background:linear-gradient(180deg,#0c0a12,#170f20)">
    <div class="toggle" style="left:28px;top:10px"><div class="seg"><svg width="20" height="20" viewBox="0 0 24 24" fill="none" stroke="currentColor" stroke-width="1.8"><rect x="3" y="7" width="13" height="10" rx="2"/><path d="M16 11l5-3v8l-5-3"/></svg>Online</div><div class="seg ring"><svg width="20" height="20" viewBox="0 0 24 24" fill="none" stroke="currentColor" stroke-width="1.8"><path d="M12 21s-7-6-7-11a7 7 0 0114 0c0 5-7 11-7 11z"/><circle cx="12" cy="10" r="2.5"/></svg>On-site</div></div>
    <div class="abs" style="left:28px;top:100px;width:501px;height:73px;border-radius:37px;border:1.5px solid #27232c;background:#100d15"><div class="abs" style="left:8px;top:7px;right:8px;bottom:7px;border-radius:30px;background:#221f28;display:flex;align-items:center;gap:16px;padding-left:26px;font-size:18px;font-weight:500"><svg width="22" height="22" viewBox="0 0 24 24" fill="none" stroke="#f06aa8" stroke-width="1.8" stroke-linejoin="round"><path d="M21 3L3 10l8 3 3 8z"/></svg>Main Office, Building A</div></div>
    <div class="tags" style="left:28px;top:191px"><div class="tag">SAVE TIME</div><div class="tag">INCREASE REVENUE</div><div class="tag add">+ Add</div></div>
  </section>

  <!-- Confirmation sheet -->
  <section class="confirm">
    <div class="confirm-top">
      <div class="send-badge"><svg width="34" height="34" viewBox="0 0 24 24" fill="none" stroke="#fff" stroke-width="1.9" stroke-linejoin="round"><path d="M21 3L10 14M21 3l-7 18-4-7-7-4z"/></svg></div>
      <h2>Ready to Send?</h2>
      <div class="sub">Review the details below</div>
    </div>
    <div class="row" style="top:241px"><span class="k">Recipient</span><span class="v">Acme Inc.</span></div>
    <div class="row" style="top:308px"><span class="k">Agenda</span><span class="v">Book a Meeting</span></div>
    <div class="btn-cancel">Cancel</div>
    <div class="btn-now">Send Now</div>
  </section>

  <!-- Success state -->
  <section class="sent">
    <h2>Sent!</h2>
    <p>Your message is on its way.</p>
    <div class="done">Done</div>
  </section>

</div>
</body>
</html>
```